We are working with a new commercial flooring contractor in California. They work on schools, hospitals, and government projects.
A few websites for inspiration:
https://plainrockcoverings.com (These guys are competitors and provide the same work our client does).
https://tjtilework.com (Although NOT a contractor, the simplicity of this site is stunning).
https://www.quietlantern.com (NOT a flooring contractor, but this site is modern, and has a boldness to it).
https://www.sagemeadowatelier.com/en-us (website for an Architectural office that is clean and showcases their work. I can see this working for a flooring contractor).
Thank you for taking the time to consider designing a website for us. We are web developers based in Stockton, CA, USA. Most of our projects go through the same process. Understanding this process may help you win a project with us. We custom-code all of our websites in-house. We don’t have any requirements as to what tools you use for your design, but we ask that you follow these guidelines.
IMAGES:
If you use any images or icons in the design, we ask that you have a link to the asset so we can purchase the image/icon. Most of the designs we submit do not have the customer’s images on them unless they have some great images. Be creative; show us the feeling you are trying to portray with your image choices. Use any royalty-free site you choose. We subscribe to Kestral and mainly use their images, but we can purchase images outside of Kestral.
FONTS:
We ask that you identify the fonts you’re using in the design. This can be done in a message if you want. We typically use Vantor Fonts and Kestral Fonts.
CONTENT:
We're always open to different content and ideas. We often submit designs with stock images so the client can see our vision. We typically take pictures after the website launch to use their images with our vision. Lorem Ipsum is fine for paragraphs, but we ask that you make the Headers with correct English. We want to be able to show the vision and identify the sections of the website.
INSPIRATION:
We typically add a couple of links in the brief of websites we like to help you get started in your design.
REVISIONS:
We do not often ask for revisions of the designs unless we see something in the design that may not appeal to the client. If there are slight changes that we want to make, we do that in the development process.
FEEDBACK:
We rarely give feedback on designs during the design process. We are working on many website projects and do not have the time to provide feedback. We usually respond if your request is well thought out and asks specific questions, but a note asking “feedback, please” usually goes unanswered.

```html
<!DOCTYPE html>
<html lang="en">
<head>
<meta charset="utf-8">
<title>Keelstone Flooring Construction</title>
<link href="https://fonts.googleapis.com/css2?family=Anton&family=Poppins:wght@400;500;600&display=swap" rel="stylesheet">
<style>
:root{
  --red:#dc2230;
  --red-dark:#b81a27;
  --ink:#111;
  --text:#333;
  --grey-bg:#efefef;
  --footer:#2b2b2d;
  --white:#fff;
  --wood:#c9a37a;
  --wood-dark:#a27a52;
}
*{box-sizing:border-box;margin:0;padding:0}
html,body{width:1200px;height:3854px;overflow:hidden}
body{font-family:'Poppins',sans-serif;color:var(--text);background:var(--white);position:relative}
.display{font-family:'Anton',sans-serif;text-transform:uppercase;color:var(--ink);letter-spacing:.5px;font-weight:400}
.btn{position:absolute;background:var(--red);color:var(--white);font-family:'Anton',sans-serif;text-transform:uppercase;font-size:14px;display:flex;align-items:center;justify-content:center;border-radius:3px;letter-spacing:.5px}
.abs{position:absolute}
.para{font-size:10.5px;line-height:18.2px;color:#444}

/* nav */
.nav{position:absolute;top:0;left:0;width:1200px;height:78px;background:var(--white);border-top:3px solid var(--red);box-shadow:0 2px 6px rgba(0,0,0,.06);z-index:5}
.nav-links{position:absolute;left:209px;top:30px;display:flex;gap:39px;font-size:12px;color:#222;letter-spacing:.5px}
.logo-badge{position:absolute;left:540px;top:8px;width:120px;height:120px;border-radius:50%;background:var(--white);border:3px solid var(--red);display:flex;align-items:center;justify-content:center;text-align:center;font-family:'Anton',sans-serif;font-size:17px;line-height:20px;color:var(--ink);text-transform:uppercase;box-shadow:0 3px 8px rgba(0,0,0,.12)}
.lang{position:absolute;left:915px;top:30px;font-size:11px;font-weight:600;color:#222;display:flex;align-items:center;gap:6px}

/* hero */
.hero{position:absolute;top:78px;left:0;width:1200px;height:588px;overflow:hidden;
  background:
    linear-gradient(180deg,rgba(255,255,255,0) 55%,rgba(160,120,80,.35) 100%),
    linear-gradient(100deg,#f1efec 0%,#e9e5df 30%,#dccab2 48%,#cfa980 62%,#b98c5e 100%)}
.hero-worker{position:absolute;left:700px;top:30px;width:420px;height:520px;border-radius:45% 45% 30% 30%;
  background:radial-gradient(ellipse at 50% 35%,rgba(220,40,48,.75) 0%,rgba(200,40,45,.55) 35%,rgba(60,60,65,.55) 62%,rgba(60,60,65,0) 75%)}
.hero-radiator{position:absolute;left:0;top:140px;width:150px;height:360px;background:linear-gradient(90deg,#e7e7e7,#fafafa 50%,#dcdcdc);opacity:.8}
.hero h1{position:absolute;left:209px;top:132px;font-size:71px;line-height:77px;text-shadow:3px 2px 0 rgba(220,34,48,.55)}

/* divider */
.divider{position:absolute;display:flex;align-items:center;gap:8px}
.divider i{display:block;height:2px;background:var(--red)}

.photo{position:absolute;border-radius:50%}

/* services */
.services{position:absolute;top:1127px;left:0;width:1200px;height:860px;overflow:hidden;background:linear-gradient(135deg,#e02a37,#d61f2d 55%,#c81b28)}
.services .shade{position:absolute;border-radius:50%;background:radial-gradient(circle,rgba(110,15,22,.35),rgba(110,15,22,0) 70%)}
.svc-card{position:absolute;width:253px;height:200px;background:var(--white)}
.svc-card .img{height:146px}
.svc-card p{font-family:'Anton',sans-serif;text-transform:uppercase;font-size:13px;line-height:16px;text-align:center;color:var(--ink);padding-top:11px}
.t-office{background:linear-gradient(135deg,#f2f2f2 0%,#d9dde2 40%,#3a3d45 75%,#c9ccd1 100%)}
.t-hat{background:linear-gradient(150deg,#f4f1ea 0%,#efe6d2 35%,#f2c318 60%,#e0a800 80%,#6d6d70 100%)}
.t-yellow{background:linear-gradient(160deg,#dfe3e6 0%,#f0c21a 35%,#d9a300 50%,#2f3238 75%,#9a9ea4 100%)}
.t-plan{background:linear-gradient(135deg,#fbfbfb 0%,#e6e6e6 45%,#c9b8a2 70%,#f2f2f2 100%)}
.t-blue{background:linear-gradient(160deg,#d9cbb5 0%,#2b5da8 35%,#7aa0d4 55%,#e6dccd 100%)}
.t-sign{background:linear-gradient(160deg,#3c3f46 0%,#55585f 35%,#e8e8e8 60%,#d17b3a 80%,#2d3036 100%)}
.t-frame{background:linear-gradient(135deg,#d8b48a 0%,#f1ece4 35%,#8b8f96 60%,#c49567 100%)}
.t-table{background:linear-gradient(135deg,#5a5d63 0%,#e9ecef 35%,#f7f7f7 60%,#f0c21a 90%)}

/* features */
.features{position:absolute;top:2483px;left:0;width:1200px;height:564px;background:var(--grey-bg)}
.feat{position:absolute;width:175px;height:205px;background:var(--white);text-align:center;box-shadow:0 1px 4px rgba(0,0,0,.08);color:var(--red)}
.feat svg{display:block;margin:26px auto 0;width:72px;height:60px}
.feat h3{font-family:'Anton',sans-serif;font-weight:400;text-transform:uppercase;font-size:14px;color:var(--ink);margin-top:14px;line-height:17px}
.feat p{font-size:10px;line-height:14px;color:#444;margin:6px 22px 0}
.feat.active{background:var(--red);color:var(--white)}
.feat.active h3,.feat.active p{color:var(--white)}

/* contact */
.field{position:absolute;left:209px;width:370px;border:1px solid #cfcfcf;border-radius:2px;font-size:10px;color:#aaa;padding:10px 23px}

/* footer */
.footer{position:absolute;top:3531px;left:0;width:1200px;height:323px;background:var(--footer);color:var(--white)}
.footer h4{position:absolute;top:74px;font-family:'Anton',sans-serif;font-weight:400;font-size:19px;text-transform:uppercase}
.footer ul{list-style:none;position:absolute;left:428px;top:112px;font-size:12px;line-height:21px;color:#ddd}
.social{position:absolute;top:111px;width:50px;height:50px;border-radius:50%;background:#6b6b6e}
</style>
</head>
<body>

<header class="nav">
  <nav class="nav-links"><span>HOME</span><span>ABOUT</span><span>SERVICES</span><span>CAREERS</span></nav>
  <div class="logo-badge">Keelstone<br>Flooring</div>
  <div class="btn" style="left:784px;top:21px;width:109px;height:32px;font-size:13px">Contact Us</div>
  <div class="lang">
    <svg width="20" height="20" viewBox="0 0 20 20" fill="none" stroke="#dc2230" stroke-width="1.5"><circle cx="10" cy="10" r="8.5"/><ellipse cx="10" cy="10" rx="3.5" ry="8.5"/><path d="M1.5 10h17M3 5.5h14M3 14.5h14"/></svg>
    ES <span style="color:#ccc">|</span> ENG
  </div>
</header>

<section class="hero" role="img" aria-label="Flooring installer in red shirt kneeling to lay wood-look plank floor, hammer and tools nearby">
  <div class="hero-radiator"></div>
  <div class="hero-worker"></div>
  <h1 class="display">Keelstone<br>Flooring<br>Construction</h1>
  <div class="btn" style="left:209px;top:381px;width:131px;height:38px">Contact Us</div>
</section>

<section class="about">
  <div class="photo" role="img" aria-label="Construction workers in hard hats reviewing plans" style="left:210px;top:738px;width:308px;height:308px;background:linear-gradient(135deg,#f2f2f2 0%,#c9c9c9 25%,#d8302f 45%,#9fb83a 65%,#6b6e73 100%)"></div>
  <div class="photo" role="img" aria-label="Smiling builder in orange hard hat" style="left:404px;top:887px;width:174px;height:174px;background:linear-gradient(160deg,#f0a020 0%,#e9e4dc 40%,#c8cdd3 65%,#b3262c 100%);border:4px solid #fff"></div>
  <h2 class="display abs" style="left:660px;top:722px;font-size:48px">About Us</h2>
  <div class="divider" style="left:660px;top:797px">
    <svg width="30" height="24" viewBox="0 0 30 24"><path d="M5 3 25 21M25 3 5 21" stroke="#dc2230" stroke-width="3"/><rect x="1" y="0" width="10" height="6" fill="#dc2230"/><rect x="19" y="0" width="10" height="6" fill="#dc2230"/></svg>
    <i style="width:62px"></i>
  </div>
  <p class="para abs" style="left:660px;top:840px;width:336px">Lorem Ipsum Dolor Sit Amet, Consectetur Adipiscing Elit. Suspendisse Vulputate Lectus Non Sapien Faucibus, In Convallis Urna Tristique. Praesent Lobortis Imperdiet Lacinia. Duis Urna Nibh, Pretium Non Sapien Eget, Egestas Hendrerit Erat. Nulla Molestie Consequat Ipsum Et Porta. Donec Ut Erat Ac Nulla Accumsan Accumsan. Sed Tincidunt Et Massa Quis Mattis. Suspendisse Sit Amet Quam Ut Elit Pretium Malesuada. Fusce Placerat, Lacus Nec Vulputate Faucibus, Magna Nibh</p>
  <div class="btn" style="left:660px;top:1008px;width:118px;height:39px;font-size:13px">Learn More</div>
</section>

<section class="services" role="region" aria-label="Our services">
  <div class="shade" style="left:-120px;top:40px;width:420px;height:700px"></div>
  <div class="shade" style="left:880px;top:80px;width:420px;height:760px"></div>
  <div class="shade" style="left:440px;top:10px;width:320px;height:200px"></div>
  <h2 class="display abs" style="left:0;width:1200px;text-align:center;top:57px;font-size:48px;color:#fff">Our Services</h2>
  <div class="divider" style="left:516px;top:121px">
    <i style="width:62px;background:#fff"></i>
    <svg width="30" height="24" viewBox="0 0 30 24"><path d="M5 3 25 21M25 3 5 21" stroke="#fff" stroke-width="3"/><rect x="1" y="0" width="10" height="6" fill="#fff"/><rect x="19" y="0" width="10" height="6" fill="#fff"/></svg>
    <i style="width:62px;background:#fff"></i>
  </div>
  <div class="svc-card" style="left:209px;top:173px"><div class="img t-office" role="img" aria-label="Business handshake in office"></div><p>With Insurance of<br>up to 20 million</p></div>
  <div class="svc-card" style="left:472px;top:173px"><div class="img t-hat" role="img" aria-label="Yellow hard hat and plans on desk"></div><p>Mod Rate<br>of .60 - .64</p></div>
  <div class="svc-card" style="left:736px;top:173px"><div class="img t-yellow" role="img" aria-label="Worker in yellow hard hat on site"></div><p>Ability to work<br>overnight and weekend</p></div>
  <div class="svc-card" style="left:209px;top:383px"><div class="img t-plan" role="img" aria-label="Hands sketching floor plan"></div><p>Design/Build<br>Experience</p></div>
  <div class="svc-card" style="left:472px;top:383px"><div class="img t-blue" role="img" aria-label="Engineers in blue hard hats on site"></div><p>Value Engineering<br>Analysis</p></div>
  <div class="svc-card" style="left:736px;top:383px"><div class="img t-sign" role="img" aria-label="Team signing contract"></div><p>Certified installers<br>for secure entities</p></div>
  <div class="svc-card" style="left:209px;top:593px"><div class="img t-frame" role="img" aria-label="Builder at timber frame site"></div><p>Assistance in<br>specifications and budgets</p></div>
  <div class="svc-card" style="left:472px;top:593px"><div class="img t-hat" role="img" aria-label="Yellow hard hat and plans on desk"></div><p>Negotiations with<br>suppliers and price scale</p></div>
  <div class="svc-card" style="left:736px;top:593px"><div class="img t-table" role="img" aria-label="Plans and tools on table"></div><p>Storage of materials<br>for work in progress</p></div>
</section>

<section class="careers">
  <h2 class="display abs" style="left:209px;top:2070px;font-size:48px">Careers</h2>
  <div class="divider" style="left:209px;top:2143px">
    <i style="width:62px"></i>
    <svg width="30" height="24" viewBox="0 0 30 24"><path d="M5 3 25 21M25 3 5 21" stroke="#dc2230" stroke-width="3"/><rect x="1" y="0" width="10" height="6" fill="#dc2230"/><rect x="19" y="0" width="10" height="6" fill="#dc2230"/></svg>
  </div>
  <p class="para abs" style="left:209px;top:2186px;width:336px">Lorem Ipsum Dolor Sit Amet, Consectetur Adipiscing Elit. Suspendisse Vulputate Lectus Non Sapien Faucibus, In Convallis Urna Tristique. Praesent Lobortis Imperdiet Lacinia. Duis Urna Nibh, Pretium Non Sapien Eget, Egestas Hendrerit Erat. Nulla Molestie Consequat Ipsum Et Porta. Donec Ut Erat Ac Nulla Accumsan Accumsan. Sed Tincidunt Et Massa Quis Mattis. Suspendisse Sit Amet Quam Ut Elit Pretium Malesuada. Fusce Placerat, Lacus Nec Vulputate Faucibus, Magna Nibh</p>
  <div class="btn" style="left:209px;top:2355px;width:111px;height:39px;font-size:13px">Apply Now</div>
  <div class="photo" style="left:619px;top:2051px;width:372px;height:372px;border:1px solid #f1c6ca"></div>
  <div class="photo" role="img" aria-label="Office team and site engineer in orange vest reviewing plans together" style="left:646px;top:2078px;width:318px;height:318px;background:linear-gradient(135deg,#eef0f2 0%,#2f3a55 35%,#d9dbe0 55%,#f0662a 75%,#e9eaec 100%)"></div>
</section>

<section class="features">
  <div class="feat" style="left:209px;top:66px">
    <svg viewBox="0 0 72 60" fill="none" stroke="currentColor" stroke-width="2.4" stroke-linejoin="round" aria-hidden="true"><path d="M4 44V22h18l8 12h6v10z"/><path d="M36 34 44 8l22 12-6 24H36z"/><path d="M46 16l16 8"/><circle cx="16" cy="48" r="5"/><circle cx="56" cy="48" r="5"/></svg>
    <h3>Concrete</h3><p>Lorem Ipsum Dolor Sit Consectetur Adipiscing Elit. Suspendisse</p></div>
  <div class="feat active" style="left:411px;top:66px">
    <svg viewBox="0 0 72 60" fill="none" stroke="currentColor" stroke-width="2.4" stroke-linejoin="round" aria-hidden="true"><rect x="32" y="14" width="18" height="14" rx="2"/><path d="M50 18h8M36 28v10h10M40 38v16h10V38"/><path d="M28 16h-6M28 21h-10M28 26h-6"/><path d="M38 14V6h8"/></svg>
    <h3>Coatings</h3><p>Lorem Ipsum Dolor Sit Consectetur Adipiscing Elit. Suspendisse</p></div>
  <div class="feat" style="left:613px;top:66px">
    <svg viewBox="0 0 72 60" fill="none" stroke="currentColor" stroke-width="2.4" stroke-linejoin="round" aria-hidden="true"><path d="M36 6 62 20 36 34 10 20z"/><path d="M10 28l26 14 26-14M10 36l26 14 26-14"/><path d="M23 13l26 14M49 13 23 27"/></svg>
    <h3>Tile/Tile</h3><p>Lorem Ipsum Dolor Sit Consectetur Adipiscing Elit. Suspendisse</p></div>
  <div class="feat" style="left:814px;top:66px">
    <svg viewBox="0 0 72 60" fill="none" stroke="currentColor" stroke-width="2.4" aria-hidden="true"><ellipse cx="26" cy="12" rx="8" ry="5"/><path d="M18 12v30M34 12v30"/><ellipse cx="26" cy="42" rx="8" ry="5"/><rect x="28" y="36" width="32" height="14" rx="7"/><circle cx="53" cy="43" r="3"/></svg>
    <h3>Wood</h3><p>Lorem Ipsum Dolor Sit Consectetur Adipiscing Elit. Suspendisse</p></div>
  <div class="feat" style="left:209px;top:294px">
    <svg viewBox="0 0 72 60" fill="none" stroke="currentColor" stroke-width="2.4" stroke-linejoin="round" aria-hidden="true"><path d="M32 4h8l1 6 5 2 5-4 6 6-4 5 2 5 6 1v8l-6 1-2 5 4 5-6 6-5-4-5 2-1 6h-8l-1-6-5-2-5 4-6-6 4-5-2-5-6-1v-8l6-1 2-5-4-5 6-6 5 4 5-2z"/><circle cx="36" cy="30" r="10"/></svg>
    <h3>Provisional Facilities</h3><p>Lorem Ipsum Dolor Sit Consectetur Adipiscing Elit. Suspendisse</p></div>
  <div class="feat" style="left:411px;top:294px">
    <svg viewBox="0 0 72 60" fill="none" stroke="currentColor" stroke-width="2.4" stroke-linejoin="round" aria-hidden="true"><rect x="12" y="38" width="8" height="16"/><rect x="26" y="30" width="8" height="24"/><rect x="40" y="22" width="8" height="32"/><rect x="54" y="12" width="8" height="42"/><path d="M8 56h58M12 30l14-8 14-6 16-10"/></svg>
    <h3>Steam Control<br>and Self-Leveling</h3><p>Lorem Ipsum Dolor Sit Consectetur Adipiscing Elit. Suspendisse</p></div>
  <div class="feat" style="left:613px;top:294px">
    <svg viewBox="0 0 72 60" fill="none" stroke="currentColor" stroke-width="2.4" stroke-linejoin="round" aria-hidden="true"><path d="M36 4c-7 10-10 15-10 20a10 10 0 0 0 20 0c0-5-3-10-10-20z"/><path d="M14 40h44M20 34l-6 6 6 6M52 34l6 6-6 6M12 52h48"/></svg>
    <h3>Resistant</h3><p>Lorem Ipsum Dolor Sit Consectetur Adipiscing Elit. Suspendisse</p></div>
  <div class="feat" style="left:814px;top:294px">
    <svg viewBox="0 0 72 60" fill="none" stroke="currentColor" stroke-width="2.4" stroke-linejoin="round" aria-hidden="true"><circle cx="20" cy="38" r="12"/><circle cx="20" cy="38" r="5"/><path d="M12 29 40 8h26L42 30h-10M30 46h36"/></svg>
    <h3>Rug</h3><p>Lorem Ipsum Dolor Sit Consectetur Adipiscing Elit. Suspendisse</p></div>
</section>

<section class="contact">
  <h2 class="display abs" style="left:209px;top:3104px;font-size:44px">Contact Us</h2>
  <div class="divider" style="left:209px;top:3174px">
    <i style="width:62px"></i>
    <svg width="30" height="24" viewBox="0 0 30 24"><path d="M5 3 25 21M25 3 5 21" stroke="#dc2230" stroke-width="3"/><rect x="1" y="0" width="10" height="6" fill="#dc2230"/><rect x="19" y="0" width="10" height="6" fill="#dc2230"/></svg>
  </div>
  <div class="field" style="top:3215px;height:39px">Enter Your Name</div>
  <div class="field" style="top:3266px;height:38px">Enter Your Email</div>
  <div class="field" style="top:3314px;height:99px">Message</div>
  <div class="btn" style="left:209px;top:3423px;width:370px;height:39px;font-size:14px">Submit</div>
  <div class="abs" style="left:648px;top:3130px;width:167px;height:38px;border:2px solid var(--red);border-radius:3px;color:var(--red);font-family:'Anton',sans-serif;font-size:13px;display:flex;align-items:center;justify-content:center">SEE LIST OF COUNTIES</div>
  <div class="abs" style="left:648px;top:3188px;width:342px;height:275px;background:#fff;box-shadow:0 1px 6px rgba(0,0,0,.15);padding:8px">
    <div role="img" aria-label="Map of California service area" style="width:100%;height:100%;background:linear-gradient(120deg,#cfe0c2 0%,#e6ead7 40%,#efe8d5 65%,#f3ead8 80%),linear-gradient(#000,#000);background-blend-mode:normal"></div>
  </div>
</section>

<footer class="footer">
  <div class="abs" style="left:209px;top:60px;display:flex;align-items:center;gap:10px">
    <span style="width:40px;height:40px;border-radius:50%;border:3px solid var(--red)"></span>
    <span style="font-family:'Anton',sans-serif;font-size:22px;line-height:26px;color:#fff">KEELSTONE<br>FLOORING</span>
  </div>
  <h4 style="left:428px">Links</h4>
  <ul><li>Home</li><li>About</li><li>Services</li><li>Careers</li><li>Contact</li></ul>
  <h4 style="left:548px">Contact Us</h4>
  <div class="abs" style="left:548px;top:114px;font-size:11px;line-height:17px;color:#ddd;display:flex;gap:10px">
    <svg width="12" height="16" viewBox="0 0 12 16"><path d="M6 15C2 10 1 8 1 6a5 5 0 0 1 10 0c0 2-1 4-5 9z" fill="none" stroke="#dc2230" stroke-width="1.5"/><circle cx="6" cy="6" r="2" fill="#dc2230"/></svg>
    <span>LOCATION NAME WILL BE<br>HERE NEAR THIS BUILDING 12345</span>
  </div>
  <div class="abs" style="left:548px;top:160px;font-size:11px;font-weight:600;color:#fff;display:flex;gap:10px;align-items:center">
    <svg width="14" height="14" viewBox="0 0 14 14"><path d="M3 1l2.5 3-1.5 1.5a8 8 0 0 0 4.5 4.5L10 8.5l3 2.5-1.5 2C6 13 1 8 1 2.5z" fill="none" stroke="#dc2230" stroke-width="1.4"/></svg>
    <span>PHONE:- 123-456-7890</span>
  </div>
  <h4 style="left:811px">Follow Us</h4>
  <div class="social" role="img" aria-label="Social profile link" style="left:811px"></div>
  <div class="social" role="img" aria-label="Social profile link" style="left:873px;background:var(--red)"></div>
  <div class="social" role="img" aria-label="Social profile link" style="left:934px"></div>
  <div class="abs" style="left:209px;top:270px;width:781px;height:1px;background:#555"></div>
  <p class="abs" style="left:0;width:1200px;text-align:center;top:291px;font-size:11px;color:#ddd">©2023 KEELSTONE FLOORING CONSTRUCTION. All Rights Reserved.</p>
</footer>

</body>
</html>
```